Brookvale Systems Yellow rose letterhead

I have a new logo for my company but in its current form it is too large to be used on letterhead or as a email signature. I need to have the designer use elements from the current logo and create something close to the original but more suited for smaller items.
Updates

I just uploaded a copy of our logo that does not have the weathered affect. Thanks

Industry/Entity Type

It Company

Requirements
Must have
• The design must maintain the visual effect of the current logo. It needs to include the yellow rose and the name of the company.
Nice to have
• It would be nice to maintain the stamp theme and incorporate my name, address, phone, email. etc.

```html
<!DOCTYPE html>
<html lang="en">
<head>
<meta charset="utf-8">
<title>Brookvale Systems – Letterhead</title>
<link rel="stylesheet" href="https://fonts.googleapis.com/css2?family=Carlito:ital,wght@0,400;1,400&display=swap">
<style>
  :root {
    --paper: #ffffff;
    --ink-soft: #857a72;
    --ink-warm: #6e625a;
    --brand-dark: #4a3f37;
    --stamp-yellow: #f2c230;
    --rule-yellow: #f3cf57;
  }
  html, body {
    margin: 0;
    padding: 0;
    width: 1200px;
    height: 321px;
    overflow: hidden;
    background: var(--paper);
  }
  .letterhead {
    position: relative;
    width: 1200px;
    height: 321px;
    font-family: "Carlito", "Calibri", sans-serif;
  }
  .brand {
    position: absolute;
    left: 15px;
    top: 8px;
    width: 303px;
    height: 254px;
    display: flex;
    flex-direction: column;
    align-items: center;
    justify-content: center;
    gap: 20px;
  }
  .brand-mark {
    width: 96px;
    height: 96px;
    background: var(--stamp-yellow);
  }
  .brand-name {
    margin: 0;
    font-size: 40px;
    font-weight: 400;
    line-height: 1.05;
    text-align: center;
    color: var(--brand-dark);
  }
  .brand-tagline {
    position: absolute;
    left: 0;
    width: 333px;
    top: 263px;
    margin: 0;
    text-align: center;
    font-size: 33px;
    line-height: 40px;
    white-space: nowrap;
    color: var(--ink-warm);
  }
  .divider {
    position: absolute;
    left: 333px;
    top: 8px;
    width: 2px;
    height: 288px;
    background: var(--rule-yellow);
  }
  .contact {
    position: absolute;
    left: 378px;
    top: 34px;
    font-style: italic;
    color: var(--ink-soft);
    font-size: 33px;
    line-height: 33px;
    white-space: nowrap;
  }
  .contact p { margin: 0; }
  .contact-name {
    font-size: 37px;
    line-height: 37px;
    color: var(--ink-warm);
  }
  .contact-email { margin-top: 35px !important; }
  .slogan {
    position: absolute;
    left: 378px;
    top: 263px;
    margin: 0;
    font-style: italic;
    font-size: 33px;
    line-height: 40px;
    white-space: nowrap;
    color: var(--ink-soft);
  }
</style>
</head>
<body>
  <main class="letterhead">
    <div class="brand">
      <div class="brand-mark"></div>
      <h1 class="brand-name">Brookvale<br>Systems</h1>
    </div>
    <p class="brand-tagline">The Network Builders</p>

    <div class="divider"></div>

    <address class="contact">
      <p class="contact-name">Dr. Nora Halvorsen</p>
      <p>218 Cedar Mill Road, Ste. 410</p>
      <p>Marlow Springs, TX 76501</p>
      <p>(800) 555-0147</p>
      <p class="contact-email">nora@brookvale-systems.com</p>
    </address>

    <p class="slogan">Building the Region’s Most Reliable Business Networks</p>
  </main>
</body>
</html>
```